Business cards and stationery for small forestry/oilfield consulting company
Pine Ledger Consulting Ltd
Business cards and stationery for small forestry/oilfield consulting company - Environment
Creative Brief
Professional
K.J. Dorrin Waltby
RPFT
Box 42 Site 7 RR5 Alberta, Canada T0X 9Q7
pineledger@quorvanet.ca
The name of Pine Ledger Consulting Ltd is in the logo itself, not needed to repeat unless somehow artistically beneficial
Concepts
Business Cards, Letterhead, and Envelopes

```html
<!DOCTYPE html>
<html lang="en">
<head>
<meta charset="utf-8">
<title>Pine Ledger Consulting Ltd — Stationery Concepts</title>
<link href="https://fonts.googleapis.com/css2?family=Cinzel:wght@600&family=Open+Sans:wght@400;600&display=swap" rel="stylesheet">
<style>
  :root{
    --backdrop:#3d2c20;
    --paper:#ffffff;
    --green:#1f6b55;
    --green-dark:#15503f;
    --rule:#9aa3a0;
    --ink:#4a4f4d;
    --label:#d9cfc4;
    --flap:#5c5f60;
  }
  *{margin:0;padding:0;box-sizing:border-box}
  html,body{width:1200px;height:466px;overflow:hidden;background:var(--backdrop)}
  .canvas{position:relative;width:1200px;height:466px;font-family:"Open Sans",sans-serif}
  .piece{position:absolute;background:var(--paper);overflow:hidden;box-shadow:0 2px 6px rgba(0,0,0,.35)}
  .swoosh{position:absolute;left:0;bottom:0;width:100%}
  .brand{font-family:"Cinzel",serif;font-weight:600;color:var(--green);text-align:center;line-height:1.1;letter-spacing:.5px;white-space:nowrap}
  .brand.light{color:var(--paper)}
  .contact{position:absolute;font-size:5px;line-height:1.5;color:var(--ink);white-space:nowrap;z-index:1}
  .contact.on-green{color:var(--paper)}
  .label{position:absolute;font-size:6px;letter-spacing:1px;color:var(--label);text-transform:uppercase;text-align:center}
  .section-title{left:14px;top:192px;text-align:left}
</style>
</head>
<body>
<div class="canvas">

  <p class="label section-title">Stationery Concepts</p>

  <!-- Business card front -->
  <div class="piece card-front" style="left:19px;top:222px;width:125px;height:72px">
    <div class="brand" style="position:absolute;left:4px;top:18px;width:64px;font-size:6px">Pine Ledger<br><span style="font-size:4.5px">Consulting Ltd</span></div>
    <div class="contact" style="left:72px;top:12px;font-size:3.6px">K.J. Dorrin Waltby, RPFT<br>Box 42 Site 7 RR5<br>Alberta, Canada T0X 9Q7<br>P 403-555-0148<br>C 780-555-0192<br>pineledger@quorvanet.ca</div>
    <svg class="swoosh" viewBox="0 0 125 20" height="20" preserveAspectRatio="none">
      <path d="M0 14 Q70 14 125 0 L125 20 L0 20Z" fill="var(--green)"/>
      <path d="M0 11 Q70 11 125 -2" fill="none" stroke="var(--rule)" stroke-width=".6"/>
    </svg>
  </div>
  <p class="label" style="left:19px;top:298px;width:125px">Business Card Front</p>

  <!-- Business card back -->
  <div class="piece card-back" style="left:19px;top:335px;width:125px;height:72px;background:var(--green)">
    <div class="brand light" style="position:absolute;left:0;top:28px;width:125px;font-size:6px">Pine Ledger Consulting Ltd</div>
  </div>
  <p class="label" style="left:19px;top:411px;width:125px">Business Card Back</p>

  <!-- Letterhead option 1 -->
  <div class="piece letterhead" style="left:180px;top:22px;width:336px;height:420px">
    <div class="brand" style="position:absolute;left:88px;top:24px;width:160px;font-size:14px">Pine Ledger<br><span style="font-size:8px">Consulting Ltd</span></div>
    <div class="contact" style="left:252px;top:22px">P 403-555-0148<br>C 780-555-0192<br>pineledger@quorvanet.ca<br>Box 42 Site 7 RR5<br>Alberta, Canada T0X 9Q7</div>
    <svg class="swoosh" viewBox="0 0 336 110" height="110" preserveAspectRatio="none">
      <path d="M0 92 Q220 92 336 0 L336 110 L0 110Z" fill="var(--green)"/>
      <path d="M0 86 Q216 86 336 -6" fill="none" stroke="var(--rule)" stroke-width="1"/>
    </svg>
  </div>
  <p class="label" style="left:180px;top:446px;width:336px">Letter Head Option 1</p>

  <!-- Letterhead option 2 -->
  <div class="piece letterhead" style="left:540px;top:22px;width:336px;height:420px">
    <div class="brand" style="position:absolute;left:88px;top:24px;width:160px;font-size:14px">Pine Ledger<br><span style="font-size:8px">Consulting Ltd</span></div>
    <svg class="swoosh" viewBox="0 0 336 110" height="110" preserveAspectRatio="none">
      <path d="M0 92 Q220 92 336 0 L336 110 L0 110Z" fill="var(--green)"/>
      <path d="M0 86 Q216 86 336 -6" fill="none" stroke="var(--rule)" stroke-width="1"/>
    </svg>
    <div class="contact on-green" style="left:205px;top:382px">P 403-555-0148<br>C 780-555-0192<br>pineledger@quorvanet.ca<br>Box 42 Site 7 RR5 Alberta, Canada T0X 9Q7</div>
  </div>
  <p class="label" style="left:540px;top:446px;width:336px">Letter Head Option 2</p>

  <!-- Envelope back, dark flap -->
  <div class="piece envelope-back" style="left:912px;top:22px;width:264px;height:118px">
    <svg width="264" height="118" viewBox="0 0 264 118">
      <path d="M0 0 L264 0 L264 22 Q250 58 200 60 L64 60 Q14 58 0 22Z" fill="var(--flap)"/>
      <path d="M0 22 Q14 58 64 60 L200 60 Q250 58 264 22" fill="none" stroke="#2e3031" stroke-width="1"/>
    </svg>
  </div>

  <!-- Envelope back, white flap with name -->
  <div class="piece envelope-back" style="left:912px;top:148px;width:264px;height:118px">
    <svg width="264" height="118" viewBox="0 0 264 118" style="position:absolute;left:0;top:0">
      <path d="M0 22 Q14 58 64 60 L200 60 Q250 58 264 22" fill="none" stroke="#c9cccb" stroke-width="1"/>
    </svg>
    <div class="brand" style="position:absolute;left:0;top:24px;width:264px;font-size:8px">Pine Ledger<br><span style="font-size:5px">Consulting Ltd</span></div>
  </div>

  <!-- Envelope front -->
  <div class="piece envelope-front" style="left:912px;top:276px;width:264px;height:150px">
    <div class="brand" style="position:absolute;left:12px;top:14px;width:90px;font-size:9px;text-align:left">Pine Ledger<br><span style="font-size:5.5px">Consulting Ltd</span></div>
    <div class="contact" style="left:12px;top:42px">Box 42 Site 7 RR5<br>Alberta, Canada T0X 9Q7<br>pineledger@quorvanet.ca</div>
    <svg class="swoosh" viewBox="0 0 264 50" height="50" preserveAspectRatio="none">
      <path d="M0 42 Q170 42 264 0 L264 50 L0 50Z" fill="var(--green)"/>
      <path d="M0 38 Q168 38 264 -4" fill="none" stroke="var(--rule)" stroke-width="1"/>
    </svg>
  </div>
  <p class="label" style="left:912px;top:430px;width:264px">Envelope Option 1</p>

</div>
</body>
</html>
```